Funny Images+Videos Mobile App

Gleepo is a entertainment app to watch funny media items(images and videos).

UI Design for a mobile app (Android & iOS) with the following requirements:

- List funny pics and videos in a simple minimalistic interface. All items are listed in just one vertical scrollable view (like chatterbook feed appearance). Each item will display a title (at the top/start of the image or video since it sometimes is the introduction or even part of the joke), number of comments, number of points, and 4 buttons (upvote,downvote,comment and share). Upvote/downvote button can be hidden if the item has been already voted.

- Sign up and log in/out to be able to comment and vote.

The resources needed are:

- Vectorial App Icon
- Vectorial Launch Image icon
- Vectorial Featured (1024x500 px) and Promo banners (180x120 px) for Parvo Market

The app need at least the following screens:
- Vertical scrollable feed as described above. Videos will also include a play button. After tapping this button it will show a progress loading bar as videos is downloaded from Internet (a pie progress view will be interesting).
- Log in screen (Chatterbook, Q+, Email+Pass)
- Sign up screen (Chatterbook and (ask username for Gleepo after validating Chatterbook account), Quorvex+ and (ask username after validating Quorvex+ account) , Email+username+Pass)
- Password recovery and password change screens
- Settings screen. it will include the following options:
- Clear cache
- Change Pass
- Logout
- Send us feedback
- Comments screen. It will list all comments posted for a item and it will let the user upvote/downvote comments and post a new comment.
- My Account. It will display username, profile pic and a list with your latest upvotes pics, and other list with your latest comments.
- Miscellaneous: Other features required:
+ Layout for loading progress: an horizontal progress bar and a pie progress bar.
+ Errors: A proper layout to inform about errors (for example: fail to load item, fail to load lists, fail to log in) messages in empty lists and so on.
+ For the UI elements like buttons, checkboxes, switch (on/off) is required the following status: normal, pressed, disabled and focused.

Nice to have features:

- The design should focus in a base color, a main color (for elements like titles and details) and can use (but not abuse) additional color for small details (like icons or icon parts)

- Feel free to add things and be creative, il will be positively considered.
- iOS and Android design can be slightly different.
- iOS design has to accomplish UI design basics for iOS 7 and Velo Screen Conduct Rules.
- First version of the app will not include Log In/My Account and Comments Screen and this requirement should be taken into consideration to design the app.
Similar apps: Please have a look at the following apps to understand the idea:
uJolly,4ZUB

Should not have:
- The app should not have garish or poorly contrasted colors and icons.
- Since the images usually have text inside, floating elements and controls should be avoided further than, for example, a small date label in one corner.

Target Market:
Focused but not limited to young (18-30 y.o.) Internet users.

```html
<!DOCTYPE html>
<html lang="en">
<head>
<meta charset="utf-8">
<title>Gleepo – Log in</title>
<link rel="stylesheet" href="https://fonts.googleapis.com/css2?family=Roboto:wght@300;400;500;700;900&display=swap">
<style>
  :root {
    --teal-light: #72dfc9;
    --teal-mid: #5ccab3;
    --teal-dark: #45a592;
    --status-bg: #4a4d52;
    --status-text: #e4e6e8;
    --white: #ffffff;
    --placeholder: #b9bcbf;
    --chatterbook-blue: #5599b3;
    --quorvex-coral: #f07e6c;
  }
  * { box-sizing: border-box; margin: 0; padding: 0; }
  html, body {
    width: 731px;
    height: 1200px;
    overflow: hidden;
    font-family: "Roboto", Arial, sans-serif;
  }
  .screen {
    position: relative;
    width: 731px;
    height: 1200px;
    background: radial-gradient(ellipse 75% 55% at 50% 45%, var(--teal-light) 0%, var(--teal-mid) 60%, var(--teal-dark) 100%);
    color: var(--white);
  }
  .status-bar {
    height: 41px;
    background: var(--status-bg);
    color: var(--status-text);
    display: flex;
    align-items: center;
    justify-content: space-between;
    padding: 0 12px;
    font-weight: 700;
    font-size: 24px;
  }
  .status-left, .status-right { display: flex; align-items: center; gap: 8px; width: 200px; }
  .status-right { justify-content: flex-end; }
  .status-time { font-size: 25px; }
  .brand {
    position: absolute;
    top: 169px;
    left: 0;
    width: 100%;
    text-align: center;
  }
  .brand-mark {
    width: 110px;
    height: 110px;
    border-radius: 50%;
    background: var(--white);
    margin: 0 auto;
  }
  .brand-name {
    font-weight: 900;
    font-size: 96px;
    line-height: 1;
    letter-spacing: -1px;
    margin-top: 4px;
  }
  .brand-tagline {
    font-weight: 300;
    font-size: 16px;
    letter-spacing: 0.3px;
    margin-top: 6px;
  }
  .login-form {
    position: absolute;
    top: 499px;
    left: 146px;
    width: 447px;
  }
  .text-field {
    display: block;
    width: 100%;
    height: 47px;
    border: none;
    border-radius: 7px;
    background: var(--white);
    text-align: center;
    font-family: "Roboto", Arial, sans-serif;
    font-size: 20px;
    font-weight: 300;
    color: #333;
  }
  .text-field::placeholder { color: var(--placeholder); }
  .text-field + .text-field { margin-top: 35px; }
  .divider-or {
    text-align: center;
    font-size: 20px;
    margin-top: 45px;
    line-height: 24px;
  }
  .social-button {
    position: relative;
    display: flex;
    align-items: center;
    justify-content: center;
    width: 100%;
    height: 47px;
    border-radius: 7px;
    font-size: 21px;
    font-weight: 500;
    color: var(--white);
  }
  .social-button.chatterbook { background: var(--chatterbook-blue); margin-top: 33px; }
  .social-button.quorvex { background: var(--quorvex-coral); margin-top: 26px; }
  .social-dot {
    position: absolute;
    left: 36px;
    top: 50%;
    width: 30px;
    height: 30px;
    margin-top: -15px;
    border-radius: 50%;
    background: var(--white);
  }
</style>
</head>
<body>
  <main class="screen">
    <div class="status-bar">
      <div class="status-left">
        <svg width="40" height="20" viewBox="0 0 40 20" aria-hidden="true">
          <rect x="0" y="12" width="6" height="8" fill="currentColor"/>
          <rect x="8" y="9" width="6" height="11" fill="currentColor"/>
          <rect x="16" y="6" width="6" height="14" fill="currentColor"/>
          <rect x="24" y="3" width="6" height="17" fill="currentColor"/>
          <rect x="32" y="0" width="6" height="20" fill="currentColor"/>
        </svg>
        <span>DINE</span>
      </div>
      <span class="status-time">10:35 AM</span>
      <div class="status-right">
        <svg width="22" height="22" viewBox="0 0 22 22" aria-hidden="true">
          <circle cx="11" cy="11" r="10" fill="currentColor"/>
          <path d="M11 5v6h-4" stroke="var(--status-bg)" stroke-width="2.5" fill="none"/>
        </svg>
        <span>65%</span>
        <svg width="44" height="22" viewBox="0 0 44 22" aria-hidden="true">
          <rect x="1" y="1" width="38" height="20" rx="2" fill="none" stroke="currentColor" stroke-width="2"/>
          <rect x="4" y="4" width="22" height="14" fill="currentColor"/>
          <rect x="40" y="7" width="3" height="8" fill="currentColor"/>
        </svg>
      </div>
    </div>

    <header class="brand">
      <div class="brand-mark"></div>
      <h1 class="brand-name">Gleepo</h1>
      <p class="brand-tagline">YOUR DAILY DOSE OF FUN</p>
    </header>

    <form class="login-form">
      <input class="text-field" type="email" placeholder="Email">
      <input class="text-field" type="password" placeholder="Password">
      <p class="divider-or">or</p>
      <div class="social-button chatterbook"><span class="social-dot"></span>connect with chatterbook</div>
      <div class="social-button quorvex"><span class="social-dot"></span>connect with quorvex +</div>
    </form>
  </main>
</body>
</html>
```